Stationery Design and Business Card

Incorporate recently designed new logo onto updated letterhead, with compliments slips, email footer and business cards. Must include all other professional branding that is on existing stationery. The letterhead is over 10 years old so would like it made more contemporary. Perhaps a little cleaner.
One professional brand has changed slightly. New file attached.

Target Market(s)

Clients of accounting firm Other professionals.

Industry/Entity Type

Accounting

Contact Information for Business Card

Existing business card included in stationery file upload. New logo has now been uploaded to the files provided

Requirements
Must have
• Existing professional body branding. There are color restrictions on how the branding can be used. Information about the SMSF specialist logo is included in uploaded files. As color is restricted on this branding the other elements of the stationery must fit with that.
Nice to have
• Prefer not to have too many colors that would add a lot of additional costs when having stationery printed.

```html
<!DOCTYPE html>
<html lang="en">
<head>
<meta charset="utf-8">
<title>Keel Advisory — Stationery Suite</title>
<link href="https://fonts.googleapis.com/css2?family=Open+Sans:wght@300;400;600;700&display=swap" rel="stylesheet">
<style>
:root{
  --navy:#27364a;
  --green:#6e8d3b;
  --board:#8b8b8b;
  --ink:#3d3d3d;
  --muted:#8a939c;
  --paper:#ffffff;
  --stage:#e8eae8;
}
*{box-sizing:border-box;margin:0;padding:0}
html,body{width:1200px;height:695px;overflow:hidden}
body{font-family:"Open Sans",Arial,sans-serif;background:var(--stage);position:relative;color:var(--ink)}

.board{position:absolute;left:0;top:0;width:525px;height:695px;background:var(--board)}
.stage{position:absolute;left:525px;top:0;width:675px;height:695px;background:radial-gradient(ellipse at 55% 40%,#f3f4f3 0%,var(--stage) 70%)}

.brand-mark{position:absolute;left:0;top:28px;width:525px;text-align:center;font-weight:700;font-size:92px;letter-spacing:6px;color:#3a3a3a;line-height:1}

/* business card */
.card{position:absolute;left:15px;top:180px;width:245px;height:346px;background:var(--navy);color:#fff;text-align:center}
.card .name{margin-top:104px;font-weight:700;font-size:44px;letter-spacing:3px;line-height:1}
.card .full{margin-top:26px;font-weight:300;font-size:13px}
.card .tag{margin-top:4px;font-size:6px;letter-spacing:1.6px;color:#b8c1ca}

/* letterhead */
.letterhead{position:absolute;width:249px;height:348px;background:var(--paper);overflow:hidden}
.letterhead.is-board{left:267px;top:180px}
.letterhead.is-feature{left:695px;top:114px;transform:scale(1.34);transform-origin:0 0;box-shadow:0 6px 18px rgba(0,0,0,.18)}
.lh-band{position:absolute;left:0;top:8px;width:100%;height:10px;background:var(--green)}
.lh-tab{position:absolute;right:0;top:0;width:78px;height:38px}
.lh-tab-text{position:absolute;right:8px;top:6px;width:60px;text-align:right;color:#fff;font-size:6.5px;line-height:1.15}
.lh-name{position:absolute;left:36px;top:21px;font-weight:700;font-size:10px;letter-spacing:1px;color:var(--navy)}
.lh-meta{position:absolute;left:8px;top:52px;width:56px;text-align:right;font-size:3.6px;line-height:1.5;color:#555}
.lh-meta p{margin-bottom:5px}
.lh-meta b{font-weight:600;display:block}
.lh-body{position:absolute;left:70px;top:52px;width:160px;font-size:3.8px;line-height:1.7;color:#555}
.lh-body p{margin-bottom:6px}
.signature{display:block;width:28px;height:9px;margin:3px 0 2px;background:linear-gradient(90deg,#2b2b2b,#555);opacity:.55;border-radius:3px}
.lh-contact{position:absolute;left:80px;right:14px;top:320px;display:flex;justify-content:space-between;font-size:3.2px;color:#444}
.lh-foot{position:absolute;left:0;bottom:0;width:100%;height:10px;background:var(--navy);border-top:1.5px solid var(--green);color:#fff;font-size:3.4px;text-align:right;padding:3px 10px 0}

/* envelope */
.envelope{position:absolute;left:15px;top:557px;width:245px;height:130px;background:var(--paper);overflow:hidden}
.env-name{position:absolute;left:18px;top:10px;font-weight:700;font-size:11px;letter-spacing:1px;color:var(--navy)}
.env-sub{position:absolute;left:18px;top:24px;font-size:3.4px;color:#666}
.env-window{position:absolute;left:18px;top:40px;width:72px;height:26px;background:#e2e4e6;border:1px solid #c4c8cc;border-radius:2px}
.env-tag{position:absolute;left:18px;top:72px;font-size:9px;line-height:1.1;color:#6a6f74}
.env-contact{position:absolute;left:18px;top:108px;font-size:3px;color:#666;display:flex;gap:8px}
.env-sweep{position:absolute;left:0;top:0}

/* compliments slip */
.slip{position:absolute;left:267px;top:555px;width:240px;height:132px;background:var(--paper);overflow:hidden}
.slip-note{position:absolute;left:0;top:14px;width:100%;text-align:center;font-size:4.4px;color:#555}
.slip-web{position:absolute;left:0;top:106px;width:100%;text-align:center;font-size:3.8px;color:#555}
.slip-foot{position:absolute;left:0;bottom:0;width:100%;height:9px;background:var(--navy);border-top:1.5px solid var(--green);color:#fff;font-size:3.2px;padding:2px 8px}
</style>
</head>
<body>

<section class="board">
  <div class="brand-mark">KEEL</div>

  <div class="card">
    <div class="name">KEEL</div>
    <div class="full">Keel Advisory</div>
    <div class="tag">Certified Practising Accountants</div>
  </div>

  <article class="letterhead is-board">
    <div class="lh-band"></div>
    <svg class="lh-tab" viewBox="0 0 78 38" aria-hidden="true"><polygon points="10,0 78,0 78,38 0,38" fill="var(--navy)"/></svg>
    <div class="lh-tab-text">Certified Practising Accountants</div>
    <div class="lh-name">KEEL</div>
    <div class="lh-meta">
      <p><b>Reference</b>SMSF/2024/01</p>
      <p><b>Subject</b>Annual Review</p>
      <p><b>Date</b>14.11.2024</p>
    </div>
    <div class="lh-body">
      <p>Dear Client,</p>
      <p>We thank you for your recent enquiry and are pleased to confirm the details of our engagement below. Please review the enclosed summary and contact our office with any questions.</p>
      <p>Our team will prepare your annual fund statements and lodge all returns before the due date. We will keep you informed at each stage of the process.</p>
      <p>Kind regards from all of us at the practice.</p>
      <p>Yours sincerely,<span class="signature" role="img" aria-label="Handwritten signature"></span>Mara Ellison<br>B.Bus, CPA, SSA</p>
    </div>
    <div class="lh-contact"><span>T 08 9000 0000</span><span>E office@keeladvisory.com.au</span><span>W keeladvisory.com.au</span></div>
    <div class="lh-foot">14 Harbour Lane Westport WA 6999 | ABN 00 000 000 000</div>
  </article>

  <div class="envelope">
    <svg class="env-sweep" width="245" height="130" viewBox="0 0 245 130" aria-hidden="true">
      <polygon points="150,130 245,0 245,130" fill="var(--navy)"/>
      <line x1="143" y1="130" x2="238" y2="0" stroke="var(--green)" stroke-width="2"/>
    </svg>
    <div class="env-name">KEEL</div>
    <div class="env-sub">Keel Advisory</div>
    <div class="env-window"></div>
    <div class="env-tag">Certified<br>Practising<br>Accountants</div>
    <div class="env-contact"><span>T 08 9000 0000</span><span>office@keeladvisory.com.au</span><span>keeladvisory.com.au</span></div>
  </div>

  <div class="slip">
    <div class="slip-note">Liability limited by a scheme approved under Professional Standards Legislation</div>
    <div class="slip-web">www.keeladvisory.com.au</div>
    <div class="slip-foot">14 Harbour Lane Westport WA 6999 | ABN 00 000 000 000</div>
  </div>
</section>

<section class="stage">
</section>

<article class="letterhead is-feature">
  <div class="lh-band"></div>
  <svg class="lh-tab" viewBox="0 0 78 38" aria-hidden="true"><polygon points="10,0 78,0 78,38 0,38" fill="var(--navy)"/></svg>
  <div class="lh-tab-text">Certified Practising Accountants</div>
  <div class="lh-name">KEEL</div>
  <div class="lh-meta">
    <p><b>Reference</b>SMSF/2024/01</p>
    <p><b>Subject</b>Annual Review</p>
    <p><b>Date</b>14.11.2024</p>
  </div>
  <div class="lh-body">
    <p>Dear Client,</p>
    <p>We thank you for your recent enquiry and are pleased to confirm the details of our engagement below. Please review the enclosed summary and contact our office with any questions.</p>
    <p>Our team will prepare your annual fund statements and lodge all returns before the due date. We will keep you informed at each stage of the process.</p>
    <p>Kind regards from all of us at the practice.</p>
    <p>Yours sincerely,<span class="signature" role="img" aria-label="Handwritten signature"></span>Mara Ellison<br>B.Bus, CPA, SSA</p>
  </div>
  <div class="lh-contact"><span>T 08 9000 0000</span><span>E office@keeladvisory.com.au</span><span>W keeladvisory.com.au</span></div>
  <div class="lh-foot">14 Harbour Lane Westport WA 6999 | ABN 00 000 000 000</div>
</article>

</body>
</html>
```